Harbor Petroleum Business Cards

I would like to design some options for about 10 sets of double sided business cards for our team with a raised logo with a Silver glossy finished logo. We are a privately funded upstream Oil & Gas producer drilling vertical wells in Central Oklahoma with a long term production (ROI driven) strategy that we implement through an annual drilling program. We are focused on a shallow / vertical / long life / low decline strategy. We are based in downtown Tulsa Oklahoma. I have attached a sample business card and a picture of our hallway logo which we would like to replicate on the business cards.

Target Market(s)

SEC Accredited Investors and other Oil & Gas Operators

Industry/Entity Type

Upstream Oil & Gas

Contact Information for Business Card

You can see the sample photo attached, but email / website / address / direct phone / Cell Phone / Name / Title / Fax

Font styles to use
Other font styles liked:
• Felix Titling

Colors
0054AA
0677BA
7BADD7
CADEEF
E8F1F8

Requirements
Must have
• Glossy raised logo
Nice to have
• Possibly a new logo.
Should not have
• No Greens /

```html
<!DOCTYPE html>
<html lang="en">
<head>
<meta charset="utf-8">
<title>Harbor Petroleum – Business Cards</title>
<link rel="stylesheet" href="https://fonts.googleapis.com/css2?family=Cinzel:wght@400&family=Tinos:wght@700&family=Arimo:wght@400&display=swap">
<style>
  :root {
    --canvas-bg: #e4e4e4;
    --card-dark-inner: #6a6663;
    --card-dark-outer: #3a3634;
    --card-light: #ffffff;
    --text-light: #f2f2f2;
    --text-dark: #3c3a39;
    --rule-light: #d8d8d8;
    --shadow: rgba(0, 0, 0, 0.28);
  }
  * { margin: 0; padding: 0; box-sizing: border-box; }
  html, body { width: 1200px; height: 800px; overflow: hidden; }
  body {
    background: var(--canvas-bg);
    display: flex;
    align-items: center;
    justify-content: center;
    gap: 40px;
  }
  .card {
    width: 520px;
    height: 300px;
    border-radius: 22px;
    box-shadow: 0 10px 24px var(--shadow);
    position: relative;
    overflow: hidden;
  }
  /* Back: contact side */
  .card--back {
    background: radial-gradient(ellipse at 55% 45%, var(--card-dark-inner) 0%, var(--card-dark-outer) 75%);
    color: var(--text-light);
    display: flex;
  }
  .brand-panel {
    width: 190px;
    display: flex;
    align-items: center;
    justify-content: center;
    padding: 0 14px;
  }
  .brand-name {
    font-family: "Cinzel", serif;
    font-weight: 400;
    font-size: 19px;
    line-height: 1.25;
    text-align: center;
    color: var(--text-light);
    letter-spacing: 1px;
  }
  .divider {
    width: 1px;
    background: var(--rule-light);
    margin: 36px 0;
  }
  .contact {
    padding: 30px 0 0 24px;
    font-family: "Arimo", sans-serif;
    font-size: 13px;
    line-height: 1.32;
  }
  .contact__name {
    font-family: "Tinos", serif;
    font-weight: 700;
    font-size: 17px;
    letter-spacing: 0.5px;
    text-transform: uppercase;
    margin-bottom: 2px;
  }
  .contact__address { margin-top: 12px; }
  .contact__list { list-style: none; margin-top: 12px; }
  .contact__list li { display: flex; align-items: center; gap: 8px; }
  .contact__list svg { width: 11px; height: 11px; flex: none; }
  /* Front: brand side */
  .card--front {
    background: var(--card-light);
    display: flex;
    align-items: center;
    justify-content: center;
  }
  .front-brand {
    display: flex;
    flex-direction: column;
    align-items: center;
    gap: 18px;
  }
  .front-brand__dot {
    width: 26px;
    height: 26px;
    border-radius: 50%;
    background: var(--text-dark);
  }
  .front-brand__name {
    font-family: "Cinzel", serif;
    font-weight: 400;
    font-size: 30px;
    color: var(--text-dark);
    letter-spacing: 1px;
  }
</style>
</head>
<body>
  <section class="card card--back" aria-label="Business card, contact side">
    <div class="brand-panel">
      <p class="brand-name">Harbor<br>Petroleum</p>
    </div>
    <div class="divider"></div>
    <div class="contact">
      <p class="contact__name">Dorian K. Whitfield, CPL</p>
      <p class="contact__title">Executive Vice President<br>Land, Legal &amp; Business Development</p>
      <p class="contact__address">42 East 9th Street, suite 800<br>Tulsa, OK 74120</p>
      <ul class="contact__list">
        <li>
          <svg viewBox="0 0 12 12" aria-hidden="true"><path d="M2.5 1h2l1 3-1.5 1a6 6 0 0 0 3 3l1-1.5 3 1v2c0 .6-.4 1-1 1A10 10 0 0 1 1.5 2c0-.6.4-1 1-1z" fill="currentColor"/></svg>
          555-210-4817
        </li>
        <li>
          <svg viewBox="0 0 12 12" aria-hidden="true"><rect x="1.5" y="1.5" width="9" height="9" fill="none" stroke="currentColor" stroke-width="1.3"/></svg>
          555-634-2290
        </li>
        <li>
          <svg viewBox="0 0 12 12" aria-hidden="true"><rect x="3" y="0.5" width="6" height="11" rx="1" fill="currentColor"/><rect x="4" y="2" width="4" height="6" fill="#3a3634"/></svg>
          555-718-5063
        </li>
        <li>
          <svg viewBox="0 0 12 12" aria-hidden="true"><rect x="0.5" y="2" width="11" height="8" fill="currentColor"/><path d="M1 2.5l5 4 5-4" fill="none" stroke="#3a3634" stroke-width="1"/></svg>
          DKW@HPTulsa.com
        </li>
        <li>
          <svg viewBox="0 0 12 12" aria-hidden="true"><circle cx="6" cy="6" r="5.3" fill="currentColor"/><path d="M1 6h10M6 .8c-2.4 3-2.4 7.4 0 10.4M6 .8c2.4 3 2.4 7.4 0 10.4" fill="none" stroke="#3a3634" stroke-width="0.8"/></svg>
          www.HarborPetroleumLLC.com
        </li>
      </ul>
    </div>
  </section>

  <section class="card card--front" aria-label="Business card, brand side">
    <div class="front-brand">
      <span class="front-brand__dot"></span>
      <p class="front-brand__name">Harbor Petroleum, LLC</p>
    </div>
  </section>
</body>
</html>
```